Spannish marketing agency needs redesign of powerpoint presentation for client acquisition

We want to redesign our powerpoint presentation. We use this presentation to show our clients how we work. WE NEED IT TO BE IN POWERPOINT FORMAT
The style should match the style of our logo and story brand, but apart from that we want designers to get creative.
The project must be in powerpoint format. The project must be in powerpoint format
Baja calidad de diseño
Small and medium size business owners
Digital marketing

```html
<!DOCTYPE html>
<html lang="es">
<head>
<meta charset="utf-8">
<title>Presentación de agencia — diapositivas</title>
<link href="https://fonts.googleapis.com/css2?family=Figtree:wght@400;500;600&family=Montserrat:wght@500&display=swap" rel="stylesheet">
<style>
:root{
  --board:#808080;
  --paper:#ffffff;
  --brand:#0a62d0;
  --brand-mid:#3f86dd;
  --brand-light:#a9cdf2;
  --ink:#111111;
}
*{margin:0;padding:0;box-sizing:border-box}
html,body{width:1200px;height:675px;overflow:hidden;background:var(--board)}
body{position:relative;font-family:"Figtree",Arial,sans-serif;color:var(--ink);-webkit-font-smoothing:antialiased;-moz-osx-font-smoothing:grayscale;text-rendering:geometricPrecision}
.slide{position:absolute;width:489px;height:275px;background:var(--paper);overflow:hidden;color:var(--ink)}
.slide--dafo-intro{left:60px;top:34px}
.slide--dafo-grid{left:651px;top:34px}
.slide--identity{left:60px;top:366px}
.slide--archetypes{left:651px;top:366px}

.slide-title{position:absolute;left:47px;color:var(--brand);font-family:"Montserrat",Arial,sans-serif;font-weight:500;font-size:15.4px;letter-spacing:.2px;line-height:1}

.intro-body{position:absolute;left:47px;top:58px;width:408px;font-size:8.7px;font-weight:500;line-height:12.9px;color:var(--ink)}

.quad{position:absolute;width:195px;color:var(--ink)}
.quad h3,.subhead{font-family:"Montserrat",Arial,sans-serif;font-size:8.6px;font-weight:500;line-height:1;margin-bottom:2px;color:var(--ink)}
.quad p{font-size:6.3px;line-height:8.6px;text-align:justify;color:var(--ink)}

.identity-body{position:absolute;left:47px;top:59px;width:397px;font-size:6.3px;line-height:8.66px;text-align:justify;color:var(--ink)}

.archetype-title{position:absolute;left:47px;top:38px;color:var(--brand);font-family:"Montserrat",Arial,sans-serif;font-weight:500;font-size:8.6px;line-height:1}
.archetype-intro{position:absolute;left:47px;top:50px;width:387px;font-size:6px;line-height:7px;color:var(--ink)}
.archetype-col{position:absolute;top:80px;width:95px;font-size:4px;line-height:6px;color:var(--ink)}
.archetype-col h4{font-weight:600;font-size:4px;color:var(--ink)}
.archetype-col section{margin-bottom:6px}

.decor{position:absolute}
.decor--bottom{left:0;top:196px;width:489px;height:79px;background:linear-gradient(100deg,var(--brand-light) 0%,var(--brand-mid) 45%,var(--brand) 62%,#d9e8f9 80%,var(--paper) 100%)}
.decor--identity{left:124px;top:163px;width:365px;height:112px;background:linear-gradient(120deg,var(--paper) 0%,var(--brand) 35%,var(--brand-mid) 65%,var(--brand-light) 100%)}
.decor--archetypes{left:214px;top:210px;width:275px;height:65px;background:linear-gradient(120deg,var(--paper) 0%,var(--brand) 35%,var(--brand-mid) 65%,var(--brand-light) 100%)}
</style>
</head>
<body>

<div class="slide slide--dafo-intro">
  <h1 class="slide-title" style="top:43px">ANÁLISIS DAFO</h1>
  <p class="intro-body">El análisis DAFO es un proceso que identifica las debilidades, amenazas, fortalezas y oportunidades de una empresa.<br>Este análisis te va a permitir conocer y analizar cierta información sobre tu empresa y su entorno.<br>Con el análisis de las amenazas y las oportunidades conoceremos el sector en profundidad y la situación externa a la compañía. Tenemos que tener en cuenta que una empresa se encuentra dentro de un todo y que no puede existir por si sola, si no que tiene que tener en cuenta el mercado en el que habita.<br>Del mismo modo, el análisis de las fortalezas y debilidades nos va a permitir conocer como nos encontramos referente a diversos factores internos.</p>
  <div class="decor decor--bottom" role="img" aria-label="Decoración de franjas y curvas azules"></div>
</div>

<div class="slide slide--dafo-grid">
  <h1 class="slide-title" style="top:43px">ANÁLISIS DAFO</h1>
  <div class="quad" style="left:47px;top:60px">
    <h3>DEBILIDADES</h3>
    <p>Debilidades internas de nuestra empresa. Debemos lidiar con ellas de la forma mas eficiente posible.<br>Ejemplos de esto pueden ser: falta de adaptación a los medios digitales, presupuesto ajustado, falta de eficiencia en algunos procesos ...</p>
  </div>
  <div class="quad" style="left:249px;top:60px">
    <h3>AMENAZAS</h3>
    <p>Situaciones externas a nuestra empresa que pueden poner en riesgo nuestro negocio La competencia está mejor posicionada que nosotros, grandes compañías como Mercalia se están quedando con gran parte del mercado, la publicidad es cada vez más cara ...</p>
  </div>
  <div class="quad" style="left:47px;top:125px">
    <h3>FORTALEZAS</h3>
    <p>Puntos fuertes de nuestra empresa, aquello en lo que destacamos y a lo cual le debemos sacar partido.<br>Nuestro producto o servicio es único, buenos márgenes de negocio, amplio conocimiento sobre un nicho en específico, un equipo de profesionales con gran talento, una misión inspiradora ...</p>
  </div>
  <div class="quad" style="left:249px;top:125px">
    <h3>OPORTUNIDADES</h3>
    <p>Factores externos a nuestra compania que pueden propiciar una oportunidad para nuestra empresa.<br>Sector en estado de crecimiento, falta de información de calidad en internet, capacidad de vender a otros países ...</p>
  </div>
  <div class="decor decor--bottom" role="img" aria-label="Decoración de franjas y curvas azules"></div>
</div>

<div class="slide slide--identity">
  <h1 class="slide-title" style="top:33px">IDENTIDAD CORPORATIVA</h1>
  <h2 class="subhead" style="position:absolute;left:47px;top:50px">PERSONALIDAD DE TU EMPRESA</h2>
  <p class="identity-body">Las personas creamos vínculos emocionales con otras personas, para conseguir generar vínculos emocionales con las empresas debemos por tanto personificarlas, o lo que es lo mismo; dotarlas de personalidad.<br>Crear una conexión emocional con nuestros clientes en los medios digitales es fundamental, ya que esto permitirá que nos elijan a nosotros y que se mantengas fieles a nuestra empresa.<br>El término "arquetipo" significa patrón original en griego antiguo. Olmedo utilizó el concepto de arquetipo en su teoría de la psique humana. Identificó 12 arquetipos de personajes universales y míticos que residen dentro de nuestro inconsciente colectivo.<br>Olmedo definió doce tipos primarios que representan la gama de motivaciones humanas básicas. Cada uno de nosotros tiende a tener un arquetipo dominante que domina nuestra personalidad.</p>
  <div class="decor decor--identity" role="img" aria-label="Decoración de franjas y curvas azules"></div>
</div>

<div class="slide slide--archetypes">
  <h1 class="archetype-title">HAY 12 ARQUETIPOS CLÁSICOS</h1>
  <p class="archetype-intro">Estos cubren el espectro, desde los que transmiten comodidad a los demás hasta los que crean entusiasmo.<br>Elegir el arquetipo correcto para su negocio es esencial.<br>Pero primero, revise los arquetipos clásicos y comprenda su papel en la creación de una conexión profunda con su mercado objetivo.</p>
  <div class="archetype-col" style="left:47px">
    <section><h4>EL INOCENTE</h4>Meta: Ser feliz<br>Rasgos: Se esfuerza por ser bueno, es puro, joven, optimista, sencillo, moral, romántico, leal.<br>Inconveniente: Podría ser ingenuo o aburrido<br>Nicho de marketing: empresas con valores sólidos,<br>vistas como confiables, confiables y honestas, asociadas con la moralidad, las buenas virtudes, la simplicidad, pueden ser nostálgicas.<br>Ejemplo: jabón Nubela, Frescana, papel higiénico Suavira</section>
    <section><h4>EL FORAJIDO</h4>Objetivo: romper las reglas y luchar contra la autoridad<br>Rasgos: Rebelde, iconoclasta, salvaje, allanando el camino para el cambio<br>Inconveniente: podría llevarlo demasiado lejos y ser visto de manera negativa<br>Nicho de marketing: agente de cambio, defensor de los marginados, permite que las personas se desahoguen o rompan con las convenciones<br>Ejemplo: Ruedaferro, Rebelia (Tomás Quiroga)</section>
  </div>
  <div class="archetype-col" style="left:148px">
    <section><h4>EL CHICO O CHICA NORMAL</h4>Meta: Pertenecer o conectarse con otros<br>Rasgos: con los pies en la tierra, solidario, fiel, campechano, persona de al lado, se conecta con los demás<br>Inconveniente: podría carecer de una identidad distintiva y mezclarse demasiado<br>Nicho de marketing: Toque común, virtudes sólidas, da sentido de pertenencia<br>Ejemplo: Casaobra, Trocalia</section>
    <section><h4>EL EXPLORADOR</h4>Meta: Encuentra satisfacción a través del descubrimiento y nuevas experiencias.<br>Rasgos: Inquieto, aventurero, ambicioso, individualista, independiente, pionero<br>Inconveniente: podría no encajar en la corriente principal<br>Nicho de marketing: emocionante, arriesgado, auténtico<br>Ejemplo: Capitán Ardiles, Terralto, Brío</section>
  </div>
  <div class="archetype-col" style="left:249px">
    <section><h4>EL HÉROE</h4>Objetivo: ayudar a mejorar el mundo<br>Rasgos: valiente, audaz, honorable, fuerte, confiado, inspirador<br>Inconveniente: Podría ser arrogante o distante<br>Nicho de marketing: Deje una marca positiva en el mundo, resuelva problemas importantes o permita/inspire a otros a hacerlo<br>Ejemplo: Zentra, Velmar, Perdura</section>
    <section><h4>EL CREADOR</h4>Meta: Crear algo con significado y valor perdurable<br>Rasgos: creativo, imaginativo, artístico, inventivo, emprendedor, inconformista<br>Inconveniente: podría ser perfeccionista o poco práctico<br>Nicho de marketing: visionario, ayudar a los clientes a expresar o crear y fomentar su imaginación<br>Ejemplo: Bloquín, Colorín</section>
  </div>
  <div class="archetype-col" style="left:349px">
    <section><h4>EL GOBERNANTE</h4>Objetivo: Controlar, crear orden a partir del caos.<br>Rasgos: líder, responsable, organizado, modelo a seguir, administrador<br>Inconveniente: podría carecer de una conexión común, o ser demasiado autoritario o controlador<br>Nicho de marketing: ayudar a las personas a organizarse mejor, restaurar el orden, crear más estabilidad y seguridad en un mundo caótico<br>Ejemplo: Nortex, Banco Alcor, Altamira Motors</section>
  </div>
  <div class="decor decor--archetypes" role="img" aria-label="Decoración de franjas y curvas azules"></div>
</div>

</body>
</html>
```